kvt business card

need clean and modern business card design, possibly two. Logo on front and writing on back-Full source files for logo attached-THE CHOSEN LOGO IS SQUARE KVT with KVT HOLDINGS in ALL BLUE. Please do not use any other logos from files, this is source file that includes correct logo

```html
<!DOCTYPE html>
<html lang="en">
<head>
<meta charset="utf-8">
<title>KVT Holdings – Business Card</title>
<link rel="stylesheet" href="https://fonts.googleapis.com/css2?family=Questrial&display=swap">
<style>
  :root {
    --stage: #2a2c31;
    --card-blue: #3a7cc4;
    --card-dark: #1f2226;
    --brand-blue: #3a7cc4;
    --accent-lime: #9ccb3b;
    --ink-white: #ffffff;
    --ink-soft: #e6e8ea;
  }
  * { box-sizing: border-box; margin: 0; padding: 0; }
  html, body {
    width: 1200px; height: 800px; overflow: hidden;
    background: var(--stage);
    font-family: "Questrial", "Helvetica Neue", Arial, sans-serif;
  }
  .stage {
    width: 1200px; height: 800px;
    display: flex; flex-direction: column; align-items: center; justify-content: center;
    gap: 60px;
  }
  .card {
    width: 525px; height: 300px; border-radius: 22px;
    position: relative; overflow: hidden;
  }

  /* Front */
  .card--front {
    background: var(--card-blue);
    display: flex; flex-direction: column; align-items: center; justify-content: center;
    color: var(--ink-white);
  }
  .front-mark {
    width: 74px; height: 74px; border-radius: 50%;
    border: 7px solid var(--ink-white);
    margin-bottom: 22px;
  }
  .brand-name {
    font-size: 34px; letter-spacing: 3px; line-height: 1; font-weight: 400;
  }
  .brand-tagline {
    margin-top: 10px; font-size: 11.5px; letter-spacing: 1.6px;
  }

  /* Back */
  .card--back {
    background: var(--card-dark);
    padding: 48px 0 0 40px;
  }
  .back-mark {
    position: absolute; right: 40px; top: 50px;
    width: 170px; height: 170px; border-radius: 50%;
    border: 12px solid var(--brand-blue);
  }
  .card--back .brand-name {
    color: var(--brand-blue); font-size: 27px; letter-spacing: 2px;
  }
  .card--back .brand-tagline {
    color: var(--accent-lime); margin-top: 6px; font-size: 9.5px; letter-spacing: 1.2px;
  }
  .person { margin-top: 26px; }
  .person-name {
    color: var(--brand-blue); font-size: 17px; letter-spacing: 1.5px;
  }
  .person-role {
    color: var(--accent-lime); font-size: 12px; margin-top: 2px;
  }
  .contact { margin-top: 18px; list-style: none; color: var(--ink-soft); font-size: 11.5px; line-height: 1.55; }
  .contact li { display: flex; align-items: center; gap: 6px; }
  .contact .icon { width: 11px; height: 11px; fill: var(--accent-lime); flex: none; }
  .contact .no-icon { padding-left: 17px; }
  .contact .web { display: block; letter-spacing: 2.5px; }
  .web-domain { color: var(--brand-blue); }
</style>
</head>
<body>
<main class="stage">

  <section class="card card--front" aria-label="Card front">
    <div class="front-mark" aria-hidden="true"></div>
    <h1 class="brand-name">KVT HOLDINGS</h1>
    <p class="brand-tagline">KEYSTONE VALLEY TRADE GROUP</p>
  </section>

  <section class="card card--back" aria-label="Card back">
    <div class="back-mark" aria-hidden="true"></div>
    <h2 class="brand-name">KVT HOLDINGS</h2>
    <p class="brand-tagline">KEYSTONE VALLEY TRADE GROUP</p>

    <div class="person">
      <p class="person-name">JORAN PELLICK</p>
      <p class="person-role">Director</p>
    </div>

    <ul class="contact">
      <li class="no-icon">PO BOX 456, Market Road</li>
      <li class="no-icon">4th Lane, Nevada</li>
      <li>
        <svg class="icon" viewBox="0 0 24 24" aria-hidden="true"><path d="M6.6 10.8a15 15 0 0 0 6.6 6.6l2.2-2.2a1 1 0 0 1 1-.25 11.4 11.4 0 0 0 3.6.57 1 1 0 0 1 1 1V20a1 1 0 0 1-1 1A17 17 0 0 1 3 4a1 1 0 0 1 1-1h3.5a1 1 0 0 1 1 1c0 1.25.2 2.45.57 3.57a1 1 0 0 1-.25 1z"/></svg>
        <span>(555) 010 2468</span>
      </li>
      <li>
        <svg class="icon" viewBox="0 0 24 24" aria-hidden="true"><path d="M2 5h20v14H2z"/><path d="M2 5l10 8 10-8" fill="none" stroke="var(--card-dark)" stroke-width="2"/></svg>
        <span>info@kvtmail.com</span>
      </li>
      <li class="no-icon web">www.<span class="web-domain">kvtholdings</span>.com</li>
    </ul>
  </section>

</main>
</body>
</html>
```